physio rehab flyer for Vela Motion please

Specification:
Flyer is to be trifold from letter size (8.5 x 11)
-----------------------This may help you:--------------------------
I would like the look of :
clean, minimalistic look with mainly blue and green
san serif font
professional
The colors I like are blue (not the blue in the logo enclosed, I want a change, but more like the blue on my website logo) and light green.
This is my website: www.velamotiongroup.ca just so you get an idea but it will be totally changed soon to a to be determined design.
I like the blue and green in file "sample 2" (enclosed)
I like the pictures in "sample 2" file enclosed
For inspiration, I like design of this brochure: http://www.qlx.ca/HarbourRestore/PatientsFamilies/Clinics_Tests/DAWL_Service/Documents/Brochure.pdf
Here's how I see the pages layout:
----[location: this should be the cover (outside, right panel of trifold)]-----
Vela Motion Logo
Integrated Injury Rehab
Evidence-based, one-on-one care to make your recovery fast and comfortable
www.velamotiongroup.ca
---------------[location: inside, left panel]----------------------------------------
Our team leaders
[portrait here]
Harriet Osei, MD, FRCPC, MSC, CIME
Physiatrist
Dr. Osei specializes in injury rehab and sports medicine. She is highly trained having received her MD and Residency in Physiatry from Wexmoor University. Her passion is to help injured people get back to their life.
[portrait here]
Dorothy Varga, PT
Physiotherapist
Dorothy has over 10 years of experience as a Physiotherapist (5 in Canada). She has advanced training in orthopedics and manual therapy. She loves and relates well with people from the youngest to the most senior.
--------------------[location: inside, middle panel]-------------------------------
Our services
We provide integrated assessment and care from interprofessional team of regulated healthcare professionals with proven experience in injury rehabilitation:
physiatrists
sport medicine physicians
physiotherapists
chiropractors
massage therapists
acupuncturists
psychologists
We provide custom medical bracing, orthotics, orthopedic shoes, assistive devices, and medical stockings, all in one place.
----------------------[location: inside, right panel]-----------------------------------
Only registered physiotherapists
We strongly believe in consistency with your treatment plan. This means that you spend your time here one-on-one with your physiotherapist, not any students or assistants. You get consistent high quality care from a professional.
One-on-one attention
We book maximum 3 people per hour to ensure everyone gets adequate one-on-one time with their physiotherapist. This compares favorably with other clinics, who may book upwards of 5-6 per hour. The atmosphere is professional -balanced with friendly, caring and relaxed. Our highly qualified staff operate this way to help make your recovery faster and more enjoyable.
------------------------[location: outside, left panel]---------------------------------
The right rehab for your clients
Timely access to comprehensive assessment and treatment
Proven track record in injury rehabilitation
Convenient one-stop service
Customized treatment plans
Integrated, co-ordinated care
Evidence-based care applying leading best practices
Access to specialty clinics: Physiatry and Chronic Pain
-------------------------[location: outside, middle panel]--------------------------
Please call us 416-738-4062
for more information on injury rehabilitation
Vela Motion Group
8120 Tolliver Rd., Unit 9
Scarborough, ON M4K 8B2
[Please include a line art map designed based on "map" file enclosed]
To make a referral for your clients, contact velamotiongroup@brisklane.ca or fax: 416-738-4059. Thank you.
www.velamotiongroup.ca
------------------------------------------------------------------------------------------------
Target Market(s)
family doctors, ER docs, lawyers, and general public age (20-50)
Industry/Entity Type
Health And Wellness
Requirements
Must have
- san serif font
- blue and green colors
- clean, sophisticated look
Nice to have
- consumer choice award badge either on front or back of trifold
Should not have
- see above

```html
<!DOCTYPE html>
<html lang="en">
<head>
<meta charset="utf-8">
<title>Vela Motion – Trifold Brochure</title>
<link href="https://fonts.googleapis.com/css2?family=PT+Sans:ital,wght@0,400;0,700;1,400;1,700&family=PT+Serif:wght@400;700&family=Roboto+Condensed:ital,wght@1,400&display=swap" rel="stylesheet">
<style>
  :root{
    --canvas:#eeedea;
    --paper:#ffffff;
    --green-pale:#eef5e0;
    --green-soft:#dcebc4;
    --green:#8dc63f;
    --green-dark:#6c9a2a;
    --blue-light:#5a9bd5;
    --blue:#2a74b8;
    --blue-dark:#1c4f8a;
    --text-blue:#2b64a3;
    --grey-blue:#7f93a8;
    --lavender:#eceef6;
    --card-line:#9ab7c9;
    --badge-red:#9b1c23;
    --badge-gold:#d6a93a;
  }
  *{margin:0;padding:0;box-sizing:border-box}
  html,body{width:1200px;height:1000px;overflow:hidden;background:var(--canvas)}
  body{position:relative;font-family:"PT Sans",Arial,sans-serif;color:var(--text-blue)}
  .sheet{position:absolute;width:550px;height:429px;background:var(--paper);overflow:hidden;box-shadow:0 2px 8px rgba(0,0,0,.15)}
  .sheet--outside{left:22px;top:203px}
  .sheet--inside{left:593px;top:298px}
  .panel{position:absolute;top:0;height:429px}
  .abs{position:absolute}

  /* outside left */
  .panel--out-left{left:0;width:186px;background:linear-gradient(#fff 0%,#fff 40%,var(--green-pale) 100%)}
  .wave{position:absolute;left:0;top:0;width:186px;height:429px}
  .rehab-title{left:34px;top:55px;font-weight:700;font-size:15px;line-height:17px;letter-spacing:.2px}
  .rehab-title .t-blue{color:var(--blue-light)}
  .rehab-title .t-green{color:var(--green)}
  .rehab-title .t-dark{color:var(--blue)}
  .benefits{left:34px;top:145px;width:150px;list-style:none;font-family:"PT Serif",Georgia,serif;font-size:9.4px;line-height:14.6px;color:var(--blue)}
  .benefits li{padding-left:8px;text-indent:-8px}
  .benefits li::before{content:"» ";color:var(--green)}

  /* outside middle */
  .panel--out-mid{left:186px;width:177px;background:linear-gradient(#f8fbf3,var(--green-pale));text-align:center;font-size:7.6px;line-height:10px;color:var(--text-blue)}
  .panel--out-mid .abs{left:8px;width:161px}
  .phone{color:var(--green);font-weight:700;font-size:8.4px}
  .map{left:34px!important;width:108px!important;top:232px;height:85px;border:2px solid var(--blue);background:linear-gradient(135deg,#f4f8fb,#e3edf4)}
  .referral{color:var(--green-dark);font-weight:700}

  /* front */
  .panel--front{left:363px;width:187px;background:var(--green-pale)}
  .cover-photo{position:absolute;left:0;top:0;width:187px;height:375px;background:linear-gradient(180deg,#cfe3f2 0%,#a9c7df 40%,#8a9aa3 62%,#9c8a72 80%,#c9b08c 100%)}
  .cover-wave{position:absolute;left:0;top:330px;width:187px;height:60px}
  .cover-title{left:4px;top:52px;font-weight:700;font-size:20px;line-height:32px}
  .cover-title .t1{color:var(--blue-light)}
  .cover-title .t2{color:var(--green)}
  .cover-title .t3{color:var(--blue)}
  .cover-tag{left:4px;top:198px;width:120px;font-weight:700;font-size:12px;line-height:14.4px;color:var(--blue)}
  .badge{border-radius:50%;background:radial-gradient(circle,var(--badge-gold) 0 55%,var(--badge-red) 56% 100%)}
  .badge--front{left:8px;top:325px;width:36px;height:36px}
  .brand{display:flex;align-items:center;gap:4px;font-weight:700;color:var(--blue-dark)}
  .brand-dot{width:9px;height:9px;border-radius:50%;background:var(--blue)}
  .brand--front{left:104px;top:362px;font-size:12px}
  .cover-url{left:6px;top:383px;font-family:"PT Serif",Georgia,serif;font-weight:700;font-size:10px;color:var(--green-dark)}

  /* inside left */
  .panel--in-left{left:0;width:187px;background:linear-gradient(90deg,var(--green-soft),var(--green-pale))}
  .card{position:absolute;border:1.5px solid var(--card-line);border-radius:7px;background:rgba(255,255,255,.55);box-shadow:2px 2px 4px rgba(0,0,0,.12)}
  .card--md{left:57px;top:25px;width:117px;height:177px}
  .card--pt{left:37px;top:217px;width:95px;height:168px}
  .person-name{font-weight:700;font-size:10.6px;color:#333;line-height:12px}
  .person-cred{font-weight:700;font-style:italic;font-size:7.6px;color:var(--blue)}
  .person-role{font-style:italic;font-size:8px;color:var(--grey-blue)}
  .bio{font-size:6.9px;line-height:8.3px;color:var(--blue-dark)}
  .portrait{position:absolute;border:1.5px solid var(--card-line);border-radius:5px}
  .portrait--md{left:34px;top:75px;width:76px;height:95px;background:linear-gradient(160deg,#b7876a,#e9e4de 50%,#c9cfd5)}
  .portrait--pt{left:97px;top:267px;width:86px;height:92px;background:linear-gradient(160deg,#dfe6ec,#c7b0a7 55%,#9aa3b5)}

  /* inside middle */
  .panel--in-mid{left:187px;width:177px;background:var(--lavender)}
  .service-photo{position:absolute;left:0;top:0;width:177px;height:144px;background:linear-gradient(150deg,#f2f4f7 0%,#9ab8d6 35%,#e7c5ad 65%,#2d3035 100%)}
  .services-title{left:0;width:177px;top:163px;text-align:center;font-weight:700;font-size:12px;color:var(--blue);font-variant:small-caps;letter-spacing:.4px}
  .services-intro{left:14px;width:152px;top:180px;font-size:7.5px;line-height:10.6px;text-align:center;color:var(--text-blue)}
  .services-list{left:40px;top:229px;list-style:none;font-size:7.5px;line-height:10.4px;color:var(--text-blue)}
  .services-list li::before{content:"» ";color:var(--green)}
  .services-note{left:10px;width:158px;top:326px;text-align:center;font-family:"Roboto Condensed","Arial Narrow",sans-serif;font-style:italic;font-size:11.4px;line-height:16.8px;color:var(--blue-dark)}

  /* inside right */
  .panel--in-right{left:364px;width:186px;background:linear-gradient(90deg,var(--green-pale),#f4f8ec)}
  .promise{left:10px;width:166px;text-align:center;font-family:"Roboto Condensed","Arial Narrow",sans-serif;font-style:italic;font-size:8.4px;line-height:12.6px;color:var(--blue-dark)}
  .promise--one{top:34px}
  .promise--two{top:169px}
  .rule{left:12px;width:162px;height:1px;background:#c7d7b0}
  .badge--inside{left:16px;top:348px;width:42px;height:42px}
  .brand--inside{left:92px;top:360px;font-size:13px}
</style>
</head>
<body>

<!-- Outside of the trifold -->
<section class="sheet sheet--outside" aria-label="Brochure outside">
  <div class="panel panel--out-left">
    <svg class="wave" viewBox="0 0 186 429" aria-hidden="true">
      <path d="M0 150 C20 110 60 80 110 62 C140 52 165 45 186 42 L186 429 L0 429Z" fill="#e2efcf" opacity=".7"/>
    </svg>
    <h2 class="abs rehab-title">
      <span class="t-blue">THE</span><br><span class="t-green">RIGHT</span><br><span class="t-blue">REHAB FOR</span><br><span class="t-dark">YOUR CLIENTS</span>
    </h2>
    <ul class="abs benefits">
      <li>Timely access to comprehensive assessment and treatment</li>
      <li>Proven track record in injury rehabilitation</li>
      <li>Convenient one-stop service</li>
      <li>Customized treatment plans</li>
      <li>Integrated, co-ordinated care</li>
      <li>Evidence-based care applying leading best practices</li>
      <li>Access to specialty clinics: Physiatry and Chronic Pain</li>
    </ul>
  </div>

  <div class="panel panel--out-mid">
    <p class="abs" style="top:143px">Please call us <span class="phone">416-738-4062</span><br>for more information on injury rehabilitation</p>
    <p class="abs" style="top:193px">Vela Motion Group<br>8120 Tolliver Rd., Unit 9<br>Scarborough, ON M4K 8B2</p>
    <div class="abs map" role="img" aria-label="Line map of the streets around the clinic"></div>
    <p class="abs referral" style="top:328px">To make a referral for your clients,<br>contact:</p>
    <p class="abs" style="top:348px">velamotiongroup@brisklane.ca<br>fax: 416-738-4059. Thank you.</p>
    <p class="abs" style="top:376px">www.velamotiongroup.ca</p>
  </div>

  <div class="panel panel--front">
    <div class="cover-photo" role="img" aria-label="Photo of a woman running outdoors with mountains behind"></div>
    <svg class="cover-wave" viewBox="0 0 187 60" preserveAspectRatio="none" aria-hidden="true">
      <path d="M0 38 C50 30 110 8 187 0 L187 60 L0 60Z" fill="#eef5e0"/>
    </svg>
    <h1 class="abs cover-title"><span class="t1">Integrated</span><br><span class="t2">Injury</span><br><span class="t3">Rehab</span></h1>
    <p class="abs cover-tag">Evidence-based, one-on-one care to make your recovery fast and comfortable</p>
    <div class="abs badge badge--front" aria-hidden="true"></div>
    <div class="abs brand brand--front"><span class="brand-dot"></span>Vela Motion</div>
    <p class="abs cover-url">www.velamotiongroup.ca</p>
  </div>
</section>

<!-- Inside of the trifold -->
<section class="sheet sheet--inside" aria-label="Brochure inside">
  <div class="panel panel--in-left">
    <div class="card card--md">
      <div class="abs" style="left:6px;top:6px">
        <p class="person-name">Harriet Osei, MD,</p>
        <p class="person-cred">FRCPC, MSC, CIME</p>
        <p class="person-role">Physiatrist</p>
      </div>
      <p class="abs bio" style="left:60px;top:49px;width:54px">Dr. Osei specializes in injury rehab and sports medicine. She is highly trained having received her MD and Residency in Physiatry from Wexmoor University. Her</p>
      <p class="abs bio" style="left:6px;top:147px;width:106px">passion is to help injured people get back to their life.</p>
    </div>
    <div class="portrait portrait--md" role="img" aria-label="Portrait of Dr. Harriet Osei"></div>

    <div class="card card--pt">
      <div class="abs" style="left:-34px;top:5px;width:130px">
        <p class="person-name" style="padding-left:30px">Dorothy Varga, PT</p>
        <p class="person-role" style="padding-left:30px">Physiotherapist</p>
      </div>
      <p class="abs bio" style="left:-34px;top:34px;width:92px;padding-left:30px">Dorothy has over 10 years of experience as a Physiotherapist (5 in Canada). She has advanced training in orthopedics and manual therapy. She loves and relates well with people from the youngest to the most senior.</p>
    </div>
    <div class="portrait portrait--pt" role="img" aria-label="Portrait of physiotherapist Dorothy Varga"></div>
  </div>

  <div class="panel panel--in-mid">
    <div class="service-photo" role="img" aria-label="Photo of a therapist fitting a knee brace on a patient"></div>
    <h2 class="abs services-title">Our services</h2>
    <p class="abs services-intro">We provide integrated assessment and care from interprofessional team of regulated healthcare professionals with proven experience in injury rehabilitation:</p>
    <ul class="abs services-list">
      <li>Physiatrists</li>
      <li>Sport medicine</li>
      <li>Physicians</li>
      <li>Physiotherapists</li>
      <li>Chiropractors</li>
      <li>Massage therapists</li>
      <li>Acupuncturists</li>
      <li>Psychologists</li>
    </ul>
    <p class="abs services-note">We provide custom medical bracing, orthotics, orthopedic shoes, assistive devices, and medical stockings, all in one place.</p>
  </div>

  <div class="panel panel--in-right">
    <p class="abs promise promise--one">Only registered physiotherapists<br>We strongly believe in consistency with your treatment plan. This means that you spend your time here one-on-one with your physiotherapist, not any students or assistants. You get consistent high quality care from a professional.</p>
    <div class="abs rule" style="top:153px"></div>
    <p class="abs promise promise--two">One-on-one attention<br>We book maximum 3 people per hour to ensure everyone gets adequate one-on-one time with their physiotherapist. This compares favorably with other clinics, who may book upwards of 5-6 per hour. The atmosphere is professional -balanced with friendly, caring and relaxed. Our highly qualified staff operate this way to help make your recovery faster and more enjoyable.</p>
    <div class="abs rule" style="top:322px"></div>
    <div class="abs badge badge--inside" aria-hidden="true"></div>
    <div class="abs brand brand--inside"><span class="brand-dot"></span>Vela Motion</div>
  </div>
</section>

</body>
</html>
```